Cobalt Ridge

Build a simple scrollable "floating" website - Website should have polished, modern look.
Domain has been bought on NestRoster and website should be setup there.
Project Brief:
https://slides.quorvane.com/deck/7Kp2Xa9Lm4Qe8Rt1Vb6Nc3Hz5Wy0Jd/edit?share=open
Input Files:
https://www.filtravo.com/f/k3mp81zt07qvr5n/BBDXnaQGyTsC_prLJFHK8u3xb?get=0

Build

```html
<!DOCTYPE html>
<html lang="en">
<head>
<meta charset="utf-8">
<title>Cobalt Ridge Hong Kong</title>
<link href="https://fonts.googleapis.com/css2?family=Oswald:wght@300;400;500&display=swap" rel="stylesheet">
<style>
:root{
  --teal:#0f7b80;
  --teal-deep:#0b5f63;
  --orange:#c8430f;
  --orange-soft:rgba(200,67,15,.9);
  --field:#86dde2;
  --ink:#3a3a3a;
  --white:#ffffff;
  --night:#0a0a0a;
  --nav:rgba(30,34,36,.78);
}
*{margin:0;padding:0;box-sizing:border-box}
html,body{width:1200px;height:2432px;overflow:hidden}
body{position:relative;background:var(--white);font-family:'Oswald',sans-serif;color:var(--ink)}
.abs{position:absolute}

/* hero */
.hero-photo{left:0;top:0;width:1200px;height:597px;
  background:
    radial-gradient(ellipse 420px 160px at 820px 230px,rgba(214,150,140,.75),transparent 70%),
    radial-gradient(ellipse 300px 120px at 180px 240px,rgba(120,95,60,.8),transparent 70%),
    radial-gradient(ellipse 260px 80px at 1080px 180px,rgba(70,95,50,.7),transparent 70%),
    linear-gradient(180deg,#6f95ad 0%,#8aa7b5 10%,#b59a8c 25%,#c49584 40%,#8d6d4e 58%,#6b5236 80%,#4e3c28 100%)}
.navbar{left:0;top:57px;width:1200px;height:70px;background:var(--nav)}
.brand{left:99px;top:17px;width:150px;height:150px;border-radius:50%;background:var(--teal);border:5px solid var(--white);
  display:flex;align-items:center;justify-content:center;text-align:center;color:var(--white);font-size:20px;font-weight:500;letter-spacing:2px;line-height:1.15}
.nav-links{left:359px;top:57px;height:70px;display:flex;align-items:center;gap:30px;color:var(--white);font-size:16px;letter-spacing:2.2px;font-weight:400}
.social{top:79px;width:26px;height:26px;border-radius:50%;background:var(--white)}
.cta{left:931px;top:73px;width:170px;height:36px;background:var(--orange);color:var(--white);font-size:14px;letter-spacing:2px;display:flex;align-items:center;justify-content:center}
.title-band{left:99px;top:529px;width:1002px;height:68px;background:var(--teal);color:var(--white);font-size:44px;font-weight:300;letter-spacing:7px;display:flex;align-items:center;justify-content:center}
.intro{left:99px;top:597px;width:1002px;height:68px;background:var(--white);box-shadow:0 4px 8px rgba(0,0,0,.25);font-size:15.5px;font-weight:300;letter-spacing:.6px;text-align:center;padding:10px 34px;line-height:1.55}

/* features */
.feature{top:726px;width:260px;text-align:center}
.feature-icon{width:96px;height:96px;border-radius:50%;background:var(--teal);border:4px solid #dcdcdc;box-shadow:0 3px 5px rgba(0,0,0,.35);margin:0 auto;display:flex;align-items:center;justify-content:center}
.feature-label{margin-top:20px;color:var(--orange);font-size:16px;letter-spacing:2px;line-height:1.5}

/* expedition */
.expedition-bg{left:0;top:960px;width:1200px;height:445px;background:linear-gradient(180deg,#3e4f5f 0%,#3a4b58 12%,#2a4258 20%,#1f3a54 45%,#1a3248 100%)}
.video{left:527px;top:1020px;width:573px;height:325px;border:3px solid rgba(255,255,255,.3);
  background:
    radial-gradient(ellipse 260px 120px at 400px 70px,rgba(70,120,50,.95),transparent 75%),
    radial-gradient(ellipse 240px 110px at 380px 230px,rgba(150,150,145,.9),transparent 75%),
    linear-gradient(180deg,#8fa6b2 0%,#5f7f8e 25%,#3e6274 55%,#2f5060 100%)}
.play{left:783px;top:1152px}
.expedition-box{left:99px;top:1064px;width:488px;height:238px;background:var(--orange-soft);padding:36px 42px;color:var(--white)}
.expedition-box h2{font-size:32px;font-weight:400;letter-spacing:5px;margin-bottom:8px;line-height:1.2}
.expedition-box p{font-size:16px;font-weight:400;line-height:1.52;letter-spacing:.2px}

/* partners */
.partners-title{left:0;top:1455px;width:1200px;text-align:center;color:var(--teal);font-size:32px;font-weight:400;letter-spacing:6px}
.partner-row{left:0;width:1200px;display:flex;justify-content:center;align-items:center}
.partner{display:flex;align-items:center;justify-content:center;gap:14px;width:330px;color:#1e1e1e;font-size:22px;letter-spacing:2px}
.partner .mark{flex:none;width:40px;height:40px}
.mark.round{border-radius:50%}

/* contact */
.contact-photo{left:0;top:1856px;width:600px;height:455px;
  background:
    radial-gradient(ellipse 260px 260px at 250px 280px,rgba(60,70,110,.55),transparent 70%),
    linear-gradient(180deg,#d8c9b4 0%,#b9b3aa 35%,#8e8e90 60%,#3c5e7a 80%,#8a9096 100%)}
.contact-panel{left:600px;top:1856px;width:600px;height:455px;background:linear-gradient(180deg,rgba(15,123,128,.85),rgba(11,95,99,.95)),#2a6a70}
.contact-title{left:699px;top:1906px;color:var(--white);font-size:32px;letter-spacing:5px;font-weight:400}
.field{left:699px;width:402px;height:36px;background:var(--field);color:var(--teal-deep);font-size:12px;padding:10px 14px}
.field.message{height:68px}
.submit{left:699px;top:2216px;width:402px;height:35px;background:var(--orange);color:var(--white);font-size:15px;letter-spacing:2px;display:flex;align-items:center;justify-content:center}

/* footer */
.footer{left:0;top:2311px;width:1200px;height:121px;background:var(--night)}
.footer-brand{left:99px;top:2329px;width:88px;height:88px;border-radius:50%;background:var(--teal);border:3px solid var(--white);color:var(--white);font-size:11px;letter-spacing:1px;display:flex;align-items:center;justify-content:center;text-align:center;line-height:1.15}
.quick-title{left:409px;top:2327px;color:#1fa9b0;font-size:15px;letter-spacing:3px}
.quick-links{left:409px;top:2362px;color:var(--white);font-size:15px;display:grid;grid-template-columns:120px 120px;row-gap:6px;letter-spacing:.5px}
.footer-social{top:2344px;width:24px;height:24px;border-radius:50%;background:var(--teal)}
.copyright{left:760px;top:2386px;width:341px;text-align:right;color:var(--white);font-size:15px;letter-spacing:1px}
</style>
</head>
<body>

<!-- hero -->
<div class="abs hero-photo" role="img" aria-label="Rocky shoreline with litter and cans washed up at the water's edge"></div>
<div class="abs navbar"></div>
<div class="abs brand">SHORELINE<br>LOOP</div>
<nav class="abs nav-links"><span>TRASH SITES</span><span>RAW DATA</span><span>EXPEDITION</span><span>SUPPORTERS</span></nav>
<div class="abs social" style="left:843px" aria-label="Social link"></div>
<div class="abs social" style="left:877px" aria-label="Social link"></div>
<div class="abs cta">GET IN TOUCH</div>
<h1 class="abs title-band">COBALT RIDGE HONG KONG</h1>
<p class="abs intro">Results of the first ever water quality and pollution recording of Hong Kong Islands 80 kilometer coastline. The data was recorded during the 2017 Shoreline Loop Expedition.</p>

<!-- features -->
<div class="abs feature" style="left:170px">
  <div class="feature-icon">
    <svg width="52" height="52" viewBox="0 0 52 52" fill="none" stroke="#fff" stroke-width="2.5">
      <rect x="8" y="8" width="14" height="14"/><path d="M22 14h10v6"/><path d="M32 20c0 4 4 6 4 10"/>
      <path d="M4 36c6-4 10 4 16 0s10 4 16 0 10 4 12 2"/><path d="M4 44c6-4 10 4 16 0s10 4 16 0 10 4 12 2"/>
    </svg>
  </div>
  <div class="feature-label">WATER POLLUTION</div>
</div>
<div class="abs feature" style="left:470px">
  <div class="feature-icon">
    <svg width="48" height="52" viewBox="0 0 48 52" fill="none" stroke="#fff" stroke-width="2.5">
      <rect x="8" y="8" width="32" height="40" rx="2"/><rect x="17" y="4" width="14" height="8" rx="2"/>
      <path d="M15 22h18M15 29h18M15 36h12"/>
    </svg>
  </div>
  <div class="feature-label">REASEARCH REPORT BY<br>HARBOUR OPEN COLLEGE<br>HONG KONG</div>
</div>
<div class="abs feature" style="left:770px">
  <div class="feature-icon">
    <svg width="52" height="52" viewBox="0 0 52 52" fill="none" stroke="#fff" stroke-width="2.5">
      <path d="M20 6h12M22 6v14L10 44h32L30 20V6"/><circle cx="36" cy="14" r="4"/><circle cx="42" cy="24" r="3"/><path d="M16 34h20"/>
    </svg>
  </div>
  <div class="feature-label">BIOCHEMISTRY DATA</div>
</div>

<!-- expedition -->
<div class="abs expedition-bg" role="img" aria-label="Dusky sea with distant hills"></div>
<div class="abs video" role="img" aria-label="Video still of climbers traversing a rocky coastline beside green hills"></div>
<svg class="abs play" width="60" height="66" viewBox="0 0 60 66"><path d="M4 2 L56 33 L4 64 Z" fill="rgba(255,255,255,.85)"/></svg>
<section class="abs expedition-box">
  <h2>THE EXPEDITION</h2>
  <p>In May 2017 Mara Velden and Tomas Greer completed the first successful coasteering expedition of Hong Kong Island. In 6 days they climbed, swam, scrambled and hiked the entire coastline, took 51 water samples and mapped 163 trash pollution spots</p>
</section>

<!-- partners -->
<h2 class="abs partners-title">OUR PARTNERS</h2>
<div class="abs partner-row" style="top:1585px">
  <div class="partner"><span class="mark" style="background:#1e1e1e"></span>HALVARD</div>
  <div class="partner"><span class="mark round" style="background:#c8202c"></span>WAYFARERS</div>
  <div class="partner"><span class="mark" style="background:#1f8a3a"></span>HARBOUR OPEN COLLEGE</div>
</div>
<div class="abs partner-row" style="top:1722px">
  <div class="partner"><span class="mark round" style="background:#2a3c8e"></span>TIDEWATER ALLIANCE</div>
  <div class="partner"><span class="mark" style="background:#1e1e1e"></span>SUMMITLINE</div>
</div>

<!-- contact -->
<div class="abs contact-photo" role="img" aria-label="Two hikers in harnesses on a city waterfront, pointing upward"></div>
<div class="abs contact-panel"></div>
<h2 class="abs contact-title">CONTACT FORM</h2>
<div class="abs field" style="top:1969px">Name</div>
<div class="abs field" style="top:2023px">Phone</div>
<div class="abs field" style="top:2076px">Email</div>
<div class="abs field message" style="top:2130px">Message</div>
<div class="abs submit">SUBMIT</div>

<!-- footer -->
<footer class="abs footer"></footer>
<div class="abs footer-brand">SHORELINE<br>LOOP</div>
<div class="abs quick-title">QUICK LINKS</div>
<div class="abs quick-links"><span>Trash Sites</span><span>Expedition</span><span>Raw Data</span><span>Supporters</span></div>
<div class="abs footer-social" style="left:1040px" aria-label="Social link"></div>
<div class="abs footer-social" style="left:1076px" aria-label="Social link"></div>
<div class="abs copyright">Copyright © 2017 &nbsp;|&nbsp; All Rights Reserved.</div>

</body>
</html>
```